Marova Hand Wash

Design hand washes. Total 12 variants to be designed.

Variants name are:

1) MILK &OLIVE
2) Shea Butter
3) Hidden Glow
4) Cream and Peach
5) Milk and Honey
6) Amber Riddle
7) Bakhour
8) Musk
9) White Oud
10) Black Oud
11) Rose Oud
12) Oud & Sandalwood

Labels can be on transparent sticker or background colors. All variants will be differentiated by fragrances and color. Bottle will be transparent. Pumps used for dispensing will be in Black or Transparent Color.

Designers can initially present designs of 4-5 variants initially. Later based on feedback, they can work out on more.

Bottle is 400ml and shape is rectangle. Ignore the size on bottle picture. Bottle keyline is attached.

Target Market(s)

B+, B, C+

Requirements
Must have
• Some relation to the variant names

```html
<!DOCTYPE html>
<html lang="en">
<head>
<meta charset="utf-8">
<title>Marova Liquid Hand Soap Labels</title>
<link rel="stylesheet" href="https://fonts.googleapis.com/css2?family=Cinzel:wght@500&family=Kaushan+Script&family=Lora:wght@500&display=swap">
<style>
  :root {
    --canvas-bg: #f3f3f1;
    --brand-purple: #4b3a8c;
    --title-white: #ffffff;
    --volume-green: #1f3a24;
    --olive-top: #bfeee9;
    --olive-bottom: #33b3bb;
    --shea-light: #ffffff;
    --shea-dark: #857a70;
    --glow-light: #fff4fa;
    --glow-dark: #dc2d86;
    --drop-teal: #5bbfb0;
  }
  html, body {
    margin: 0;
    padding: 0;
    width: 1200px;
    height: 858px;
    overflow: hidden;
    background: var(--canvas-bg);
  }
  .label-row {
    position: relative;
    width: 1200px;
    height: 858px;
  }
  .label {
    position: absolute;
    top: 325px;
    width: 253px;
    height: 448px;
    border-radius: 20px;
    overflow: hidden;
    box-shadow: 0 2px 8px rgba(0,0,0,0.12);
  }
  .label--milk-olive { left: 79px; background: linear-gradient(180deg, var(--olive-top) 0%, var(--olive-bottom) 60%, #4cc0c6 100%); }
  .label--shea-butter { left: 479px; background: radial-gradient(ellipse at 20% 10%, var(--shea-light) 0%, #d9d3cd 35%, var(--shea-dark) 75%, #efece8 100%); }
  .label--hidden-glow { left: 882px; background: radial-gradient(ellipse at 50% 0%, var(--glow-light) 0%, #f3a3c9 35%, var(--glow-dark) 70%, #f07fb4 100%); }

  .brand-name {
    position: absolute;
    top: 58px;
    left: 0;
    width: 100%;
    text-align: center;
    font-family: "Lora", serif;
    font-weight: 500;
    font-size: 38px;
    color: var(--brand-purple);
  }
  .variant-title {
    position: absolute;
    left: 46px;
    top: 178px;
    margin: 0;
    font-family: "Cinzel", serif;
    font-weight: 500;
    font-size: 35px;
    line-height: 42px;
    color: var(--title-white);
    text-shadow: 0 1px 3px rgba(0,0,0,0.35);
  }
  .label--shea-butter .variant-title { left: 14px; }
  .label--hidden-glow .variant-title { left: 14px; letter-spacing: 1px; }
  .product-type {
    position: absolute;
    left: 18px;
    top: 280px;
    font-family: "Kaushan Script", cursive;
    font-size: 21px;
    color: var(--title-white);
  }
  .volume {
    position: absolute;
    left: 16px;
    top: 348px;
    font-family: "Lora", serif;
    font-size: 19px;
    color: var(--volume-green);
  }
  .care-drop {
    position: absolute;
    left: 210px;
    top: 228px;
    width: 38px;
    height: 46px;
  }
  .label--shea-butter .care-drop { left: 185px; }
  .label--hidden-glow .care-drop { left: 185px; }
  .ingredient-art {
    position: absolute;
  }
  .label--milk-olive .ingredient-art {
    left: 0; bottom: 0; width: 253px; height: 150px;
    background: linear-gradient(160deg, rgba(255,255,255,0) 0%, #9cc23a 40%, #ffffff 85%);
    clip-path: polygon(55% 0, 100% 0, 100% 100%, 0 100%, 0 75%, 40% 45%);
  }
  .label--shea-butter .ingredient-art {
    left: 100px; bottom: 14px; width: 145px; height: 100px;
    border-radius: 50%;
    background: radial-gradient(ellipse, #e9e4dc 0%, #6e543b 45%, rgba(110,84,59,0) 75%);
  }
  .label--hidden-glow .ingredient-art {
    left: 0; bottom: 0; width: 253px; height: 170px;
    background: linear-gradient(180deg, rgba(229,60,140,0) 0%, #c8347e 25%, #f4b6cf 65%, #fbe0ea 100%);
    clip-path: polygon(60% 0, 100% 0, 100% 100%, 0 100%, 0 50%);
  }
</style>
</head>
<body>
<main class="label-row">

  <section class="label label--milk-olive">
    <div class="brand-name">Marova</div>
    <h2 class="variant-title">Milk &amp;<br>Olive</h2>
    <svg class="care-drop" viewBox="0 0 38 46" role="img" aria-label="Drop icon with caring hands">
      <path d="M19 0 C19 0 2 20 2 29 a17 17 0 0 0 34 0 C36 20 19 0 19 0 Z" fill="#ffffff"/>
      <circle cx="19" cy="29" r="11" fill="var(--drop-teal)"/>
    </svg>
    <div class="product-type">Liquid hand soap</div>
    <div class="ingredient-art" role="img" aria-label="Green olives with leaves over a splash of milk"></div>
    <div class="volume">400ml</div>
  </section>

  <section class="label label--shea-butter">
    <div class="brand-name">Marova</div>
    <h2 class="variant-title">Shea<br>Butter</h2>
    <svg class="care-drop" viewBox="0 0 38 46" role="img" aria-label="Drop icon with caring hands">
      <path d="M19 0 C19 0 2 20 2 29 a17 17 0 0 0 34 0 C36 20 19 0 19 0 Z" fill="#ffffff"/>
      <circle cx="19" cy="29" r="11" fill="var(--drop-teal)"/>
    </svg>
    <div class="product-type">Liquid hand soap</div>
    <div class="ingredient-art" role="img" aria-label="Shea nuts with one cracked open showing white butter"></div>
    <div class="volume">400ml</div>
  </section>

  <section class="label label--hidden-glow">
    <div class="brand-name">Marova</div>
    <h2 class="variant-title">Hidden<br>Glow</h2>
    <svg class="care-drop" viewBox="0 0 38 46" role="img" aria-label="Drop icon with caring hands">
      <path d="M19 0 C19 0 2 20 2 29 a17 17 0 0 0 34 0 C36 20 19 0 19 0 Z" fill="#ffffff"/>
      <circle cx="19" cy="29" r="11" fill="var(--drop-teal)"/>
    </svg>
    <div class="product-type">Liquid hand soap</div>
    <div class="ingredient-art" role="img" aria-label="Pink rose held by a hand above a field of pink and white roses"></div>
    <div class="volume">400ml</div>
  </section>

</main>
</body>
</html>
```